Parkinson's Disease Progression

Visually describe the rate of Parkinson progression in the first 15 years following diagnosis. Title: "Patient-Perceived Progression of Parkinsonism"

The attached figure names "meanqol" is the curve that should serve as the basis of this graphic. Everything else-- color, labels, font, etc. describe this curve.
Thank you!

Target Market(s)

People with Parkisnon's Disease, neurologists, family members.

Font styles to use
Sans Serif

Requirements
Must have
• Must have the lines going through these exact numbers
Excellent -- 502
Very good- 661
Good- 895
Fair- 1268
Poor- 1655

LABELS:
Title: "Patient-Perceived Progression of Parkinsonism"
"SAW-MX (Self-Assessed Wellbeing Index for Movement Conditions)" should be the label on the left.
"Quality of Life" should be the label on the right
"Years Since Diagnosis" should be the label on the bottom
Nice to have
• A color scheme that goes from GOOD (low numbers) to BAD (high numbers).

Easy to read (elderly)

```html
<!DOCTYPE html>
<html lang="en">
<head>
<meta charset="utf-8">
<title>Patient-Perceived Progression of Parkinsonism</title>
<link href="https://fonts.googleapis.com/css2?family=Questrial&family=Oswald:wght@400;500&family=Montserrat:wght@500;600&display=swap" rel="stylesheet">
<style>
  :root{
    --page:#ececec;
    --card:#ffffff;
    --slate:#46555f;
    --slate-soft:#8fa3b3;
    --title-blue:#6f8ea8;
    --ink:#1c1c1c;
    --poor:#b98d98;
    --fair:#e8d0d3;
    --good:#f3d5b5;
    --verygood:#a7b4e2;
    --excellent:#a2cbab;
    --dot-poor:#b0707e;
    --dot-fair:#dda1ab;
    --dot-good:#dcb07f;
    --dot-verygood:#6f7fcb;
    --dot-excellent:#6fb27f;
  }
  html,body{margin:0;padding:0;width:1200px;height:1200px;overflow:hidden;background:var(--page);}
  .infographic{display:block;width:1200px;height:1200px;}
  .title-main{font-family:"Questrial",sans-serif;font-size:43px;fill:var(--title-blue);font-weight:700;}
  .title-rest{font-family:"Questrial",sans-serif;font-size:43px;fill:#fff;font-weight:700;}
  .axis-num{font-family:"Montserrat",sans-serif;font-size:22px;fill:var(--ink);font-weight:500;}
  .band-label{font-family:"Montserrat",sans-serif;font-size:14px;fill:#fff;font-weight:600;letter-spacing:.5px;}
  .index-name{font-family:"Montserrat",sans-serif;font-size:27px;fill:#fff;font-weight:600;}
  .index-full{font-family:"Montserrat",sans-serif;font-size:13.5px;fill:#fff;}
  .axis-title{font-family:"Questrial",sans-serif;font-size:29px;fill:#fff;font-weight:700;}
  .qol-label{font-family:"Montserrat",sans-serif;font-size:25px;fill:var(--slate);font-weight:600;letter-spacing:1px;}
  .score{font-family:"Oswald",sans-serif;font-size:23px;font-weight:500;text-anchor:middle;}
</style>
</head>
<body>
<svg class="infographic" viewBox="0 0 1200 1200" xmlns="http://www.w3.org/2000/svg">
  <defs>
    <linearGradient id="qolGradient" x1="0" y1="0" x2="0" y2="1">
      <stop offset="0" stop-color="#b98d98"/>
      <stop offset=".45" stop-color="#e9b89c"/>
      <stop offset=".75" stop-color="#d9d2a8"/>
      <stop offset="1" stop-color="#9fcfaa"/>
    </linearGradient>
  </defs>

  <!-- card -->
  <rect class="card" x="32" y="182" width="1138" height="802" fill="var(--card)"/>

  <!-- header -->
  <g class="header">
    <rect x="32" y="182" width="1138" height="101" fill="var(--slate)"/>
    <rect x="32" y="196" width="738" height="65" rx="4" fill="#fff"/>
    <polygon points="64,212 78,228 64,244" fill="var(--slate)"/>
    <text class="title-main" x="93" y="243">Patient-Perceived Progression</text>
    <text class="title-rest" x="780" y="243">of Parkinsonism</text>
  </g>

  <!-- left index label -->
  <g class="index-panel">
    <path d="M32 362 H82 A26 26 0 0 1 108 388 V824 A26 26 0 0 1 82 850 H32 Z" fill="var(--slate-soft)"/>
    <text class="index-name" transform="translate(73 672) rotate(-90)">SAW-MX</text>
    <text class="index-full" transform="translate(91 805) rotate(-90)">(Self-Assessed Wellbeing Index for Movement Conditions)</text>
  </g>

  <!-- y axis -->
  <g class="y-axis">
    <line x1="180" y1="417" x2="195" y2="417" stroke="var(--ink)" stroke-width="1.5"/>
    <line x1="180" y1="491" x2="195" y2="491" stroke="var(--ink)" stroke-width="1.5"/>
    <line x1="180" y1="565" x2="195" y2="565" stroke="var(--ink)" stroke-width="1.5"/>
    <line x1="180" y1="638" x2="195" y2="638" stroke="var(--ink)" stroke-width="1.5"/>
    <line x1="180" y1="712" x2="195" y2="712" stroke="var(--ink)" stroke-width="1.5"/>
    <line x1="180" y1="786" x2="195" y2="786" stroke="var(--ink)" stroke-width="1.5"/>
    <text class="axis-num" transform="translate(159 491) rotate(-90)" text-anchor="middle">1000</text>
    <text class="axis-num" transform="translate(159 565) rotate(-90)" text-anchor="middle">800</text>
    <text class="axis-num" transform="translate(159 638) rotate(-90)" text-anchor="middle">600</text>
    <text class="axis-num" transform="translate(159 712) rotate(-90)" text-anchor="middle">400</text>
    <text class="axis-num" transform="translate(159 786) rotate(-90)" text-anchor="middle">200</text>
    <g class="people-icon" fill="var(--slate-soft)">
      <circle cx="140" cy="824" r="5"/><circle cx="151" cy="820" r="5.5"/><circle cx="162" cy="824" r="5"/>
      <rect x="131" y="832" width="40" height="22" rx="10"/>
    </g>
  </g>

  <!-- bands -->
  <g class="bands">
    <rect x="245" y="362" width="720" height="30" fill="var(--poor)"/>
    <rect x="245" y="392" width="720" height="138" fill="var(--fair)"/>
    <rect x="245" y="530" width="720" height="86" fill="var(--good)"/>
    <rect x="245" y="616" width="720" height="59" fill="var(--verygood)"/>
    <rect x="245" y="675" width="720" height="165" fill="var(--excellent)"/>
    <g stroke="#333" stroke-width="1.2" stroke-dasharray="2 3">
      <line x1="245" y1="392" x2="965" y2="392"/>
      <line x1="245" y1="530" x2="965" y2="530"/>
      <line x1="245" y1="616" x2="965" y2="616"/>
      <line x1="245" y1="675" x2="965" y2="675"/>
    </g>
    <rect x="245" y="362" width="720" height="478" fill="none" stroke="var(--ink)" stroke-width="1.5"/>
  </g>

  <!-- band labels strip -->
  <g class="band-strip">
    <rect x="195" y="362" width="50" height="478" fill="var(--slate)"/>
    <text class="band-label" x="196" y="384">POOR</text>
    <text class="band-label" transform="translate(226 485) rotate(-90)">FAIR</text>
    <text class="band-label" transform="translate(226 596) rotate(-90)">GOOD</text>
    <text class="band-label" transform="translate(217 672) rotate(-90)">VERY</text>
    <text class="band-label" transform="translate(233 670) rotate(-90)">GOOD</text>
    <text class="band-label" transform="translate(226 818) rotate(-90)">EXCELLENCE</text>
  </g>

  <!-- curves -->
  <g class="curves" fill="none" stroke="var(--ink)">
    <path d="M313 672 C360 648 395 625 430 604 C470 582 530 588 590 582 C640 576 670 552 700 530 C760 496 820 476 940 457" stroke-width="2"/>
    <path d="M306 655 C350 634 395 612 440 592 C490 572 540 580 600 568 C650 556 690 528 720 510 C790 470 840 440 897 402" stroke-width="1.6" stroke-dasharray="6 5"/>
    <path d="M328 684 C370 660 405 636 445 616 C495 594 550 598 605 594 C650 590 685 562 720 538 C790 512 840 500 875 500 C905 500 925 503 940 508" stroke-width="1.6" stroke-dasharray="6 5"/>
  </g>

  <!-- x axis -->
  <g class="x-axis">
    <line x1="267" y1="840" x2="940" y2="840" stroke="var(--ink)" stroke-width="1.5"/>
    <line x1="267" y1="840" x2="267" y2="856" stroke="var(--ink)" stroke-width="1.5"/>
    <line x1="491" y1="840" x2="491" y2="856" stroke="var(--ink)" stroke-width="1.5"/>
    <line x1="715" y1="840" x2="715" y2="856" stroke="var(--ink)" stroke-width="1.5"/>
    <line x1="940" y1="840" x2="940" y2="856" stroke="var(--ink)" stroke-width="1.5"/>
    <text class="axis-num" x="267" y="896" text-anchor="middle">0</text>
    <text class="axis-num" x="491" y="896" text-anchor="middle">5</text>
    <text class="axis-num" x="715" y="896" text-anchor="middle">10</text>
    <text class="axis-num" x="940" y="896" text-anchor="middle">15</text>
    <path class="hourglass-icon" d="M206 853 H230 M206 885 H230 M209 853 L218 869 L209 885 M227 853 L218 869 L227 885" stroke="var(--slate-soft)" stroke-width="3" fill="none"/>
  </g>

  <!-- score markers -->
  <g class="markers" stroke-width="3">
    <circle cx="281" cy="676" r="29" fill="#fff" stroke="var(--dot-excellent)"/>
    <text class="score" x="281" y="685" fill="var(--dot-excellent)" stroke="none">502</text>
    <circle cx="416" cy="611" r="29" fill="#fff" stroke="var(--dot-verygood)"/>
    <text class="score" x="416" y="620" fill="var(--dot-verygood)" stroke="none">661</text>
    <circle cx="700" cy="525" r="29" fill="#fff" stroke="var(--dot-good)"/>
    <text class="score" x="700" y="534" fill="var(--dot-good)" stroke="none">895</text>
    <circle cx="918" cy="415" r="29" fill="#fff" stroke="var(--dot-fair)"/>
    <text class="score" x="918" y="424" fill="var(--dot-fair)" stroke="none">1268</text>
    <circle cx="963" cy="364" r="29" fill="#fff" stroke="var(--dot-poor)"/>
    <text class="score" x="963" y="373" fill="var(--dot-poor)" stroke="none">1655</text>
  </g>

  <!-- quality of life scale -->
  <g class="qol-scale">
    <circle cx="1078" cy="323" r="21" fill="var(--poor)"/>
    <rect x="1060" y="385" width="38" height="457" rx="19" fill="url(#qolGradient)"/>
    <path d="M1026 425 L1079 372 L1132 425" fill="none" stroke="var(--poor)" stroke-width="26" stroke-linecap="round" stroke-linejoin="round"/>
    <circle cx="1078" cy="871" r="21" fill="var(--excellent)"/>
    <text class="qol-label" transform="translate(1088 738) rotate(-90)">QUALITY OF LIFE</text>
  </g>

  <!-- x axis title -->
  <g class="x-title">
    <path d="M198 968 V936 A26 26 0 0 1 224 910 H939 A26 26 0 0 1 965 936 V968 Z" fill="var(--slate-soft)"/>
    <path d="M390 924 H416 M390 960 H416 M393 924 L403 942 L393 960 M413 924 L403 942 L413 960" stroke="#fff" stroke-width="3" fill="none"/>
    <text class="axis-title" x="433" y="952">Years Since Diagnosis</text>
  </g>

  <!-- footer bar -->
  <rect x="32" y="968" width="1138" height="16" fill="var(--slate)"/>
</svg>
</body>
</html>
```